Business cards for Brightmarrow Consulting with the following info for the front side:

Brightmarrow Consulting
Executive Coaching and Human Capital Strategy
www.brightmarrow.example

Lorena Vaduvic
Principal
lorena@brightmarrow.example
+1 604 555 0172

Black background, text using the colours of the logo - enclosed.

The back side of the business card should feature the logo in the middle, with "Executive Coaching and Human Capital Strategy" on top and "www.brightmarrow.example" below.

```html
<!DOCTYPE html>
<html lang="en">
<head>
<meta charset="utf-8">
<title>Brightmarrow Consulting – Business Cards</title>
<link href="https://fonts.googleapis.com/css2?family=Arimo:wght@400;700&display=swap" rel="stylesheet">
<style>
  :root {
    --backdrop: #3a3a3c;
    --card: #050505;
    --brand-blue: #2aa6dd;
    --brand-yellow: #f3c316;
    --ink-light: #f2f2f2;
  }
  html, body {
    margin: 0;
    padding: 0;
    width: 1200px;
    height: 1200px;
    overflow: hidden;
    background: var(--backdrop);
    font-family: "Arimo", Arial, sans-serif;
  }
  .stage {
    position: relative;
    width: 1200px;
    height: 1200px;
  }
  .card {
    position: absolute;
    left: 250px;
    width: 700px;
    height: 400px;
    background: var(--card);
    box-shadow: 0 14px 30px rgba(0,0,0,0.45);
    box-sizing: border-box;
    color: var(--ink-light);
  }
  .card--back {
    top: 150px;
    border-radius: 90px 0 90px 0;
    display: flex;
    flex-direction: column;
    align-items: center;
    justify-content: center;
    text-align: center;
  }
  .card--front {
    top: 630px;
    border-radius: 0 90px 0 90px;
    padding: 60px 0 0 150px;
  }
  .tagline {
    font-size: 17px;
    letter-spacing: 1px;
    line-height: 1.1;
    text-transform: uppercase;
    margin: 0 0 52px;
  }
  .wordmark {
    display: flex;
    align-items: center;
    gap: 14px;
  }
  .wordmark__dot {
    width: 52px;
    height: 52px;
    border-radius: 50%;
    background: var(--brand-yellow);
    flex: none;
  }
  .wordmark__name {
    font-weight: 700;
    font-size: 36px;
    letter-spacing: 2px;
    color: var(--brand-blue);
    text-transform: uppercase;
  }
  .web {
    color: var(--brand-blue);
    letter-spacing: 0.5px;
  }
  .web__domain { color: var(--brand-yellow); }
  .card--back .web {
    font-size: 17px;
    text-transform: uppercase;
    margin-top: 52px;
  }
  .person {
    margin: 46px 0 0 50px;
  }
  .person__name {
    font-weight: 700;
    font-size: 21px;
    color: var(--brand-blue);
    text-transform: uppercase;
    letter-spacing: 0.5px;
    margin: 0;
  }
  .person__role {
    font-size: 17px;
    margin: 2px 0 0;
  }
  .contacts {
    list-style: none;
    margin: 28px 0 0 26px;
    padding: 0;
    font-size: 18px;
  }
  .contacts li {
    display: flex;
    align-items: center;
    gap: 10px;
    height: 26px;
  }
  .contacts svg {
    width: 20px;
    height: 20px;
    flex: none;
  }
</style>
</head>
<body>
<main class="stage">

  <section class="card card--back" aria-label="Card back">
    <p class="tagline">Executive Coaching and<br>Human Capital Strategy</p>
    <div class="wordmark">
      <span class="wordmark__dot"></span>
      <span class="wordmark__name">Brightmarrow</span>
    </div>
    <p class="web">www.<span class="web__domain">brightmarrow</span>.example</p>
  </section>

  <section class="card card--front" aria-label="Card front">
    <div class="wordmark">
      <span class="wordmark__dot"></span>
      <span class="wordmark__name">Brightmarrow</span>
    </div>
    <div class="person">
      <p class="person__name">Lorena Vaduvic</p>
      <p class="person__role">Principal</p>
    </div>
    <ul class="contacts">
      <li>
        <svg viewBox="0 0 20 20" aria-hidden="true">
          <rect x="1.5" y="1.5" width="17" height="17" rx="2" fill="none" stroke="var(--brand-blue)" stroke-width="1.6"/>
          <path d="M6.5 5.5 l2 0 l1 2.5 l-1.3 1 a6 6 0 0 0 2.8 2.8 l1-1.3 l2.5 1 l0 2 a1.2 1.2 0 0 1 -1.3 1.1 A8.5 8.5 0 0 1 5.4 6.8 a1.2 1.2 0 0 1 1.1 -1.3z" fill="var(--brand-blue)"/>
        </svg>
        <span>+1 604 555 0172</span>
      </li>
      <li>
        <svg viewBox="0 0 20 20" aria-hidden="true">
          <rect x="1" y="4" width="18" height="12" fill="var(--brand-blue)"/>
          <path d="M1 4 L10 11 L19 4" fill="none" stroke="var(--card)" stroke-width="1.4"/>
        </svg>
        <span>lorena@brightmarrow.example</span>
      </li>
      <li>
        <svg viewBox="0 0 20 20" aria-hidden="true" fill="none" stroke="var(--brand-blue)" stroke-width="1.5">
          <circle cx="10" cy="10" r="8.5"/>
          <ellipse cx="10" cy="10" rx="3.8" ry="8.5"/>
          <path d="M1.5 10 H18.5 M3 5.5 H17 M3 14.5 H17"/>
        </svg>
        <span class="web">www.<span class="web__domain">brightmarrow</span>.example</span>
      </li>
    </ul>
  </section>

</main>
</body>
</html>
```